4K Business Card Design

We need a business card that emphasizes consulting services worldwide. The name of the company is KKKK Consulting Group. We provide consulting services across several industries including but not limited to commodities, telecom, manufacturing, logistics, marketing and operations. We would like to see a creative design that emphasizes the global aspect, including Latin America and US markets, as well the bilingual nature of the service offerings.

The contact information section should include icons to represent the following data:
1) Name, Title and Company Name
2) Mobile Number
3) Skype ID
4) Email
5) Web Page
6) Location

We would like to see a card that emphasizes the worldwide concept. The back of the card should be simple, including only the logo (or a portion of the logo) and the slogan.

We would also like to see business cards in a booklet format. The colors to be used should be the same combination of colors used in the logos attached to this brief.

The logo design and some business card examples from Artful Herd are attached for reference on style and look.

Target Market(s)

International business executives, 45-65 years of age, bilingual

Industry/Entity Type

Marketing

Colors
0792cd
34a7d8
85cae6
ffffff
cee9f5
ecf7fb

Requirements
Must have
• Please follow colors in logo attached.

2) Mobile Number
3) Skype ID
4) Email
5) Web Page
6) Location
Nice to have
• Global concept, consulting profile, diverse industry focus
Should not have
• No black color

```html
<!DOCTYPE html>
<html lang="en">
<head>
<meta charset="utf-8">
<title>KKKK Consulting Group – Business Card</title>
<link rel="stylesheet" href="https://fonts.googleapis.com/css2?family=Open+Sans:wght@400;600&family=Cinzel:wght@400&display=swap">
<style>
  :root{
    --stage:#3b3c3f;
    --card-white:#ffffff;
    --brand-blue:#5f98c2;
    --brand-blue-deep:#5089b5;
    --brand-blue-light:#6ea6cd;
    --stripe-grey:#8199aa;
    --ink:#4a4d52;
    --name-blue:#5a97c8;
    --rule-blue:#a9c6dc;
  }
  *{box-sizing:border-box;margin:0;padding:0}
  html,body{width:1200px;height:946px;overflow:hidden;background:var(--stage)}
  .canvas{position:relative;width:1200px;height:946px}
  .card{position:absolute;left:250px;width:700px;height:400px;overflow:hidden;border-radius:3px;box-shadow:0 10px 24px rgba(0,0,0,.35)}
  .card--back{top:48px;background:linear-gradient(135deg,var(--brand-blue-light),var(--brand-blue-deep))}
  .card--front{top:498px;background:var(--card-white)}

  .back-mark{position:absolute;left:0;top:0;width:100%;height:100%;display:flex;align-items:center;justify-content:center;gap:14px}
  .back-mark__square{width:26px;height:26px;background:#fff}
  .back-mark__name{font-family:"Open Sans",sans-serif;font-weight:600;font-size:56px;letter-spacing:6px;color:#fff}

  .front-band{position:absolute;left:0;top:0}

  .divider{position:absolute;left:378px;top:70px;width:2px;height:215px;transform:rotate(-14deg);background:linear-gradient(to bottom,rgba(169,198,220,0),var(--rule-blue) 40%,rgba(169,198,220,0))}

  .company{position:absolute;left:40px;top:150px;width:320px;text-align:center}
  .company__mark{display:block;width:30px;height:30px;margin:0 auto 16px;background:var(--brand-blue)}
  .company__name{font-family:"Cinzel",serif;font-weight:400;font-size:25px;line-height:1.25;color:var(--brand-blue)}

  .contact{position:absolute;left:430px;top:82px;font-family:"Open Sans",sans-serif;color:var(--ink)}
  .contact__name{font-size:21px;font-weight:600;color:var(--name-blue);line-height:1.1}
  .contact__title{font-size:14px;line-height:1.3}
  .contact__list{list-style:none;margin-top:32px}
  .contact__item{display:flex;align-items:center;gap:7px;font-size:15px;line-height:21px}
  .contact__icon{width:13px;height:13px;flex:none;fill:var(--brand-blue)}
</style>
</head>
<body>
<main class="canvas">
  <section class="card card--back" aria-label="Card back">
    <div class="back-mark">
      <span class="back-mark__square"></span>
      <span class="back-mark__name">KKKK</span>
    </div>
  </section>

  <section class="card card--front" aria-label="Card front">
    <svg class="front-band" width="700" height="400" viewBox="0 0 700 400" aria-hidden="true">
      <polyline points="0,372 428,372 450,300" fill="none" stroke="#8199aa" stroke-width="7"/>
      <polygon points="0,381 436,381 460,304 700,304 700,400 0,400" fill="#5f98c2"/>
    </svg>

    <div class="divider"></div>

    <div class="company">
      <span class="company__mark"></span>
      <p class="company__name">KKKK Consulting Group</p>
    </div>

    <div class="contact">
      <p class="contact__name">Lena Ortiz</p>
      <p class="contact__title">President &amp; CEO</p>
      <ul class="contact__list">
        <li class="contact__item">
          <svg class="contact__icon" viewBox="0 0 16 16"><path d="M8 1 1 8h2v7h4v-4h2v4h4V8h2z"/></svg>
          Bayview Isles, FL
        </li>
        <li class="contact__item">
          <svg class="contact__icon" viewBox="0 0 16 16"><path d="M4 0h8v16H4zM5.5 2v10h5V2z"/></svg>
          +1 305 555-0148
        </li>
        <li class="contact__item">
          <svg class="contact__icon" viewBox="0 0 16 16"><path d="M0 3h16v10H0zM1.5 4.5 8 9l6.5-4.5z" fill-rule="evenodd"/></svg>
          k4cg@mailnest.com
        </li>
        <li class="contact__item">
          <svg class="contact__icon" viewBox="0 0 16 16"><circle cx="8" cy="8" r="7"/></svg>
          k4consultinggroup
        </li>
      </ul>
    </div>
  </section>
</main>
</body>
</html>
```